Prescription Savings Card

Looking to revamp our cards that are distributed to pharmacies. Processing information must stand out and be in black with lines through zeros for easy identification.
I have included some previous card designs for consideration. we are looking to go with something cleaner with mainly processing information on the back similar to all white version attached.
Target Market(s)
Pharmacists and Pharmacy Technicians
Industry/Entity Type
prescription medications
Contact Information for Business Card
processing information
Requirements
Must have
- easy to read processing information

```html
<!DOCTYPE html>
<html lang="en">
<head>
<meta charset="utf-8">
<title>MedPass Prescription Savings Card</title>
<link href="https://fonts.googleapis.com/css2?family=Ubuntu:wght@400;500;700&display=swap" rel="stylesheet">
<style>
  :root {
    --backdrop: #3f3f8e;
    --card-white: #ffffff;
    --card-black: #1e1e1e;
    --brand-blue: #2e2f8f;
    --accent-red: #e0262b;
    --band-dark: #333333;
    --band-mid: #4e4e4e;
    --band-light: #8a8a8a;
    --text-dark: #111111;
    --text-light: #ffffff;
  }
  * { box-sizing: border-box; margin: 0; padding: 0; }
  html, body { width: 1200px; height: 1000px; overflow: hidden; }
  body {
    background: var(--backdrop);
    font-family: "Ubuntu", Arial, sans-serif;
    display: flex;
    align-items: center;
    justify-content: center;
    gap: 60px;
  }
  .savings-card {
    width: 520px;
    height: 328px;
    border-radius: 18px;
    overflow: hidden;
    display: flex;
    flex-direction: column;
    box-shadow: 0 6px 18px rgba(0,0,0,0.25);
  }
  .savings-card--white { background: var(--card-white); color: var(--text-dark); }
  .savings-card--black { background: var(--card-black); color: var(--text-light); }

  .card-brand {
    height: 68px;
    flex: none;
    display: flex;
    align-items: center;
    justify-content: center;
  }
  .brand-name {
    font-size: 42px;
    font-weight: 700;
    letter-spacing: -1px;
    color: var(--brand-blue);
    line-height: 1;
  }

  .card-band {
    height: 138px;
    flex: none;
    background:
      radial-gradient(ellipse 70% 140% at 18% 120%, rgba(255,255,255,0.16), transparent 60%),
      linear-gradient(100deg, var(--band-dark) 0%, var(--band-mid) 45%, var(--band-light) 78%, var(--band-mid) 100%);
    display: flex;
    justify-content: space-between;
    align-items: center;
    padding: 0 26px 0 22px;
    color: var(--text-light);
  }
  .benefit-list { list-style: none; display: flex; flex-direction: column; gap: 9px; }
  .benefit-list li {
    display: flex; align-items: center; gap: 9px;
    font-size: 15.5px; font-weight: 500;
    white-space: nowrap;
    line-height: 1.2;
  }
  .benefit-list svg { width: 15px; height: 10px; flex: none; }

  .processing-info {
    display: grid;
    grid-template-columns: auto auto auto;
    column-gap: 10px;
    row-gap: 1px;
    font-size: 18px;
    font-weight: 700;
    line-height: 1.15;
    white-space: nowrap;
  }

  .card-notice {
    flex: 1;
    text-align: center;
    display: flex;
    flex-direction: column;
    align-items: center;
    justify-content: center;
    padding: 4px 16px 8px;
  }
  .notice-title {
    font-size: 18px;
    font-weight: 500;
    letter-spacing: 0.5px;
    line-height: 1.2;
  }
  .notice-rule {
    width: 300px; height: 2px; margin: 5px auto 7px;
    background: linear-gradient(90deg, transparent, var(--accent-red), transparent);
  }
  .notice-text { font-size: 13px; line-height: 1.3; }
  .notice-admin { font-size: 11.5px; font-weight: 500; margin-top: 3px; line-height: 1.2; }
</style>
</head>
<body>

  <article class="savings-card savings-card--white">
    <header class="card-brand"><span class="brand-name">MedPass</span></header>
    <section class="card-band">
      <ul class="benefit-list">
        <li><svg viewBox="0 0 16 10"><path d="M1 1 L8 5 L1 9 M7 1 L14 5 L7 9" fill="none" stroke="#e0262b" stroke-width="2"/></svg>Save up to 99%</li>
        <li><svg viewBox="0 0 16 10"><path d="M1 1 L8 5 L1 9 M7 1 L14 5 L7 9" fill="none" stroke="#e0262b" stroke-width="2"/></svg>100% HIPAA Compliant</li>
        <li><svg viewBox="0 0 16 10"><path d="M1 1 L8 5 L1 9 M7 1 L14 5 L7 9" fill="none" stroke="#e0262b" stroke-width="2"/></svg>Lower Price Guarentee</li>
        <li><svg viewBox="0 0 16 10"><path d="M1 1 L8 5 L1 9 M7 1 L14 5 L7 9" fill="none" stroke="#e0262b" stroke-width="2"/></svg>Cover 90 Days Supply &amp; Pet Meds</li>
      </ul>
      <div class="processing-info">
        <span>BIN</span><span>:</span><span>014820</span>
        <span>ID</span><span>:</span><span>MP0000</span>
        <span>PCN</span><span>:</span><span>MDPS2</span>
        <span>GROUP</span><span>:</span><span>MDPASS</span>
        <span>CONDOR</span><span>:</span><span>36805</span>
      </div>
    </section>
    <footer class="card-notice">
      <h2 class="notice-title">ATTENTION PHARMACY</h2>
      <div class="notice-rule"></div>
      <p class="notice-text">If you are unable to process a prescription through our program<br>please call (800)-555-0142</p>
      <p class="notice-admin">Administrated by Halden Health - This is NOT INSURANCE</p>
    </footer>
  </article>

  <article class="savings-card savings-card--black">
    <header class="card-brand"><span class="brand-name">MedPass</span></header>
    <section class="card-band">
      <ul class="benefit-list">
        <li><svg viewBox="0 0 16 10"><path d="M1 1 L8 5 L1 9 M7 1 L14 5 L7 9" fill="none" stroke="#e0262b" stroke-width="2"/></svg>Save up to 99%</li>
        <li><svg viewBox="0 0 16 10"><path d="M1 1 L8 5 L1 9 M7 1 L14 5 L7 9" fill="none" stroke="#e0262b" stroke-width="2"/></svg>100% HIPAA Compliant</li>
        <li><svg viewBox="0 0 16 10"><path d="M1 1 L8 5 L1 9 M7 1 L14 5 L7 9" fill="none" stroke="#e0262b" stroke-width="2"/></svg>Lower Price Guarentee</li>
        <li><svg viewBox="0 0 16 10"><path d="M1 1 L8 5 L1 9 M7 1 L14 5 L7 9" fill="none" stroke="#e0262b" stroke-width="2"/></svg>Cover 90 Days Supply &amp; Pet Meds</li>
      </ul>
      <div class="processing-info">
        <span>BIN</span><span>:</span><span>014820</span>
        <span>ID</span><span>:</span><span>MP0000</span>
        <span>PCN</span><span>:</span><span>MDPS2</span>
        <span>GROUP</span><span>:</span><span>MDPASS</span>
        <span>CONDOR</span><span>:</span><span>36805</span>
      </div>
    </section>
    <footer class="card-notice">
      <h2 class="notice-title">ATTENTION PHARMACY</h2>
      <div class="notice-rule"></div>
      <p class="notice-text">If you are unable to process a prescription through our program<br>please call (800)-555-0142</p>
      <p class="notice-admin">Administrated by Halden Health - This is NOT INSURANCE</p>
    </footer>
  </article>

</body>
</html>
```